An anniversary gift for my girlfriend

My girlfriend and I have been dating for almost 2 years. We met online and this has afforded us the really unique opportunity to have the first words we said to each other (the whole conversation, in fact) preserved. We're moving in together in a few months and she doesn't know that I saved the conversation. I've been waiting for this to turn it into something we can hang in our new place.

The only phrase I want to use is:
"Well if you dislike people's knees then I think we'll get along famously"

It's an Never Quite Dusk in Marlowe Bay reference for the curious.

I want the poster to use the words themselves as the art; I'm thinking typography. I'd like it to match her aesthetic, she likes to wear Tessa Brook and R. Vane. Colors shouldn't be anything too "girly". Somewhere I'd like to include the date June 1, 2015. It shouldn't be a major piece of the poster though, just a way to denote the date.

It should fit (and be fully visible in) a 16x20 (inches) frame

Thanks in advance for the work!

Industry/Entity Type

Dating

Font styles to use
Serif
Decorative
Script

Requirements
Must have
• Must use only the words: "Well if you dislike people's knees then I think we'll get along famously"
• I want this to be typography, so making the phrase the center of the poster and the art itself.

```html
<!DOCTYPE html>
<html lang="en">
<head>
<meta charset="utf-8">
<title>Well If You Dislike People's Knees — Anniversary Poster</title>
<link rel="stylesheet" href="https://fonts.googleapis.com/css2?family=Cormorant+SC:wght@500&family=Montserrat:wght@400;500;800&family=Raleway:wght@100&display=swap">
<style>
  :root {
    --ink: #3d2317;
    --peach-light: #fbe0c4;
    --peach: #f6c39a;
    --apricot: #ee9f74;
    --cream: #f4ecd2;
    --sun: #f3d27e;
  }
  html, body {
    margin: 0;
    padding: 0;
    overflow: hidden;
    background: var(--cream);
  }
  .poster {
    display: block;
    width: 960px;
    height: 1200px;
  }
  .word-serif {
    font-family: "Cormorant SC", "Times New Roman", serif;
    font-weight: 500;
    fill: var(--ink);
  }
  .word-thin {
    font-family: "Raleway", "Helvetica Neue", sans-serif;
    font-weight: 100;
    fill: var(--ink);
  }
  .word-heavy {
    font-family: "Montserrat", "Arial Black", sans-serif;
    font-weight: 800;
    fill: var(--ink);
  }
  .word-regular {
    font-family: "Montserrat", Arial, sans-serif;
    font-weight: 400;
    fill: var(--ink);
  }
  .date-line {
    font-family: "Montserrat", Arial, sans-serif;
    font-weight: 500;
    fill: var(--ink);
  }
</style>
</head>
<body>
<svg class="poster" viewBox="0 0 960 1200" xmlns="http://www.w3.org/2000/svg">
  <defs>
    <linearGradient id="wash" x1="0" y1="0" x2="1" y2="1">
      <stop offset="0" stop-color="var(--peach-light)"/>
      <stop offset="0.5" stop-color="var(--peach)"/>
      <stop offset="0.8" stop-color="var(--cream)"/>
      <stop offset="1" stop-color="var(--cream)"/>
    </linearGradient>
    <radialGradient id="bloom-left" cx="0.5" cy="0.5" r="0.5">
      <stop offset="0" stop-color="var(--sun)" stop-opacity="0.8"/>
      <stop offset="1" stop-color="var(--sun)" stop-opacity="0"/>
    </radialGradient>
    <radialGradient id="bloom-right" cx="0.5" cy="0.5" r="0.5">
      <stop offset="0" stop-color="var(--sun)" stop-opacity="0.6"/>
      <stop offset="1" stop-color="var(--sun)" stop-opacity="0"/>
    </radialGradient>
  </defs>

  <g class="background">
    <rect class="watercolor-wash" width="960" height="1200" fill="url(#wash)" role="img" aria-label="Soft peach and cream watercolour wash with paint splatters"/>
    <circle class="sun-disc" cx="480" cy="492" r="420" fill="var(--apricot)" opacity="0.7"/>
    <ellipse class="flowers-left" cx="200" cy="1010" rx="280" ry="230" fill="url(#bloom-left)" role="img" aria-label="Watercolour daisies in white and pale yellow"/>
    <ellipse class="flowers-right" cx="800" cy="1080" rx="200" ry="160" fill="url(#bloom-right)" role="img" aria-label="Sketched yellow wildflowers"/>
  </g>

  <g class="phrase">
    <text class="word-serif" x="114" y="234" font-size="190" textLength="480" lengthAdjust="spacingAndGlyphs">WELL</text>
    <text class="word-thin" x="606" y="198" font-size="50" textLength="276" lengthAdjust="spacingAndGlyphs">IF YOU</text>
    <text class="word-heavy" x="612" y="234" font-size="50" textLength="270" lengthAdjust="spacingAndGlyphs">DISLIKE</text>

    <text class="word-heavy" x="96" y="348" font-size="112" textLength="784" lengthAdjust="spacingAndGlyphs">PEOPLE'S KNEES</text>

    <text class="word-serif" x="114" y="504" font-size="190" textLength="456" lengthAdjust="spacingAndGlyphs">THEN</text>
    <text class="word-heavy" x="606" y="434" font-size="50" textLength="276" lengthAdjust="spacingAndGlyphs">I THINK</text>
    <text class="word-thin" x="606" y="504" font-size="54" textLength="276" lengthAdjust="spacingAndGlyphs">WE'LL</text>

    <text class="word-heavy" x="96" y="630" font-size="140" textLength="786" lengthAdjust="spacingAndGlyphs">GET ALONG</text>
    <text class="word-regular" x="96" y="770" font-size="156" textLength="786" lengthAdjust="spacingAndGlyphs">FAMOUSLY</text>
  </g>

  <text class="date-line" x="336" y="854" font-size="34" textLength="284" lengthAdjust="spacingAndGlyphs">JUNE 1, 2015</text>
</svg>
</body>
</html>
```